MES Modul-Struktur grafisch veranschaulichen
Zielgruppe
Wir sind Software-Hersteller. Thema 'MES'. Unsere Kunden sind Produktionsunternehmen.
Mit einem MES (Manufacturing Execution System) werden Produktionsprozesse überwacht, geplant, gesteuert und optimiert. Allgemein geht es darum, die Produktivität zu steigern und Kosten zu minimieren.
Eine MES-Software ist modular strukturiert, so dass der Kunde sich nach Bedarf die einzelnen Funktionsmodule zusammenstellen kann. Unser MES MORVIK 7 MAX besteht z.B. aus folgenden Einzelmodulen:
- BASIS (Basismodul)
- MDE (Maschinendatenerfassung)
- BDE (Betriebsdatenerfassung)
- INST (Instandhaltung)
- ALARM (Alarmierung)
- DOK (Dokumentenmanagement)
- TNT (Traceability)
- PLAN (Feinplanung/Leitstand)
- LOG (Logistik)
- VIS (Visualisierung)
- PEP (Personaleinsatzplanung)
- MPZE (Personalzeiterfassung)
- DNC (Rezepturen/DNC)
- EM (Energiemonitoring)
Aufgabenstellung
Die modulare Struktur und der große Umfang an Modulen ist ein wichtiger Vorteil für unsere Kunden, da Sie nicht so schnell an Grenzen stoßen und sich dann unter Umständen eine weitere Insellösung (extra Software mit extra Datenbank ...) anschaffen müssen.
Wichtig ist, dass die einzelnen Module funktionell ineinandergreifen und alle auf die gleiche Datenbank zugreifen.
Es reicht wenn in der Grafik die Module nur mit er Abkürzung, also z.B. MDE bezeichnet werden. Für den ersten Entwurf können auch Platzhalter genutzt werden.
Der Betrachter sollte aus der Grafik auf den ersten Blick erkennen:
- umfängliches MES
- modular strukturiert
- Funktionsmodule step-by-step erweiterbar
Für die Umsetzung naheliegend wären Puzzle-Steine, Stapolos, ... muss aber nicht.

```html
<!DOCTYPE html>
<html lang="de">
<head>
<meta charset="utf-8">
<title>MES Modulstruktur</title>
<link rel="stylesheet" href="https://fonts.googleapis.com/css2?family=Ubuntu:wght@400;700&display=swap">
<style>
  :root{
    --bg-center:#ffffff;
    --bg-edge:#dde1e5;
    --frame:#6e6e6e;
    --tile:#ffffff;
    --label:#ffffff;
  }
  html,body{margin:0;padding:0;overflow:hidden;background:#fff;}
  .canvas{width:1200px;height:857px;display:block;}
  .frame{fill:none;stroke:var(--frame);stroke-width:1.5;}
  .tile{fill:var(--tile);}
  .band-top{fill:var(--dark);}
  .band-bottom{fill:var(--light);}
  .module-code{font-family:"Ubuntu",sans-serif;font-weight:700;font-size:23px;fill:var(--label);text-anchor:middle;}
  .module-name{font-family:"Ubuntu",sans-serif;font-weight:400;font-size:11px;fill:var(--label);text-anchor:middle;}
  .badge-back{fill:var(--tile);}
  .badge-ring{fill:var(--tile);stroke:var(--dark);stroke-width:2.6;}
  .icon{fill:none;stroke:var(--dark);stroke-width:2.4;stroke-linecap:round;stroke-linejoin:round;}
  .icon-fill{fill:var(--dark);stroke:none;}
  .m-basis{--dark:#bccdd8;--light:#cbd8e1;}
  .m-bde{--dark:#f8b000;--light:#f9c240;}
  .m-inst{--dark:#ee7f00;--light:#f19a3c;}
  .m-alarm{--dark:#e84e1b;--light:#ec7240;}
  .m-dok{--dark:#e2001a;--light:#e54c3c;}
  .m-mde{--dark:#b5cb22;--light:#c7d75c;}
  .m-tnt{--dark:#00962f;--light:#4ba857;}
  .m-pep{--dark:#7fc4e8;--light:#9cd1ee;}
  .m-vis{--dark:#3398d1;--light:#66a8d6;}
  .m-em{--dark:#1b5fa3;--light:#4673b0;}
  .m-plan{--dark:#ec7cad;--light:#f09bc0;}
  .m-mpze{--dark:#b8358c;--light:#c463a3;}
  .m-dnc{--dark:#6b2e72;--light:#875489;}
  .m-log{--dark:#372a66;--light:#5d457f;}
</style>
</head>
<body>
<svg class="canvas" viewBox="0 0 1200 857" xmlns="http://www.w3.org/2000/svg" xmlns:xlink="http://www.w3.org/1999/xlink">
  <defs>
    <radialGradient id="backdrop" cx="50%" cy="45%" r="65%">
      <stop offset="0%" stop-color="var(--bg-center)"/>
      <stop offset="55%" stop-color="#f4f5f6"/>
      <stop offset="100%" stop-color="var(--bg-edge)"/>
    </radialGradient>
    <filter id="tile-shadow" x="-30%" y="-30%" width="160%" height="160%">
      <feDropShadow dx="0" dy="3" stdDeviation="5" flood-color="#000" flood-opacity="0.22"/>
    </filter>
    <polygon id="tile-shape" points="0,-107 92.7,-53.5 92.7,53.5 0,107 -92.7,53.5 -92.7,-53.5"/>
    <polygon id="band-top" points="0,-88.5 76.6,-44.25 76.6,-4 -76.6,-4 -76.6,-44.25"/>
    <polygon id="band-bottom" points="-76.6,-4 76.6,-4 76.6,44.25 0,88.5 -76.6,44.25"/>
    <g id="badge">
      <circle class="badge-back" r="33"/>
      <circle class="badge-ring" r="29"/>
    </g>
  </defs>

  <rect width="1200" height="857" fill="url(#backdrop)"/>
  <rect class="frame" x="0.75" y="0.75" width="1198.5" height="855.5"/>

  <!-- BASIS -->
  <g class="module m-basis" transform="translate(598.5 138)">
    <use class="tile" href="#tile-shape" filter="url(#tile-shadow)"/>
    <use class="band-top" href="#band-top"/><use class="band-bottom" href="#band-bottom"/>
    <text class="module-code" y="-41">BASIS</text>
    <text class="module-name" y="-22">Basismodul</text>
    <g transform="translate(0 38)">
      <use href="#badge"/>
      <path class="icon-fill" d="M0,19 C-6,9 -13,2 -13,-6 A13,13 0 0 1 13,-6 C13,2 6,9 0,19Z"/>
      <circle cx="0" cy="-6" r="4.5" fill="#fff"/>
    </g>
  </g>

  <!-- Row 2 -->
  <g class="module m-bde" transform="translate(281 319)">
    <use class="tile" href="#tile-shape" filter="url(#tile-shadow)"/>
    <use class="band-top" href="#band-top"/><use class="band-bottom" href="#band-bottom"/>
    <text class="module-code" y="-41">BDE</text>
    <text class="module-name" y="-21">Betriebsdatenerfassung</text>
    <g transform="translate(0 38)">
      <use href="#badge"/>
      <path class="icon" d="M-16,-15 V15 H17 M-11,13 V-4 M-6,13 V-10 M-1,13 V2 M4,13 V6"/>
      <circle class="icon" cx="4" cy="-4" r="7"/>
      <path class="icon" d="M9,1 L16,9"/>
    </g>
  </g>

  <g class="module m-inst" transform="translate(493 319)">
    <use class="tile" href="#tile-shape" filter="url(#tile-shadow)"/>
    <use class="band-top" href="#band-top"/><use class="band-bottom" href="#band-bottom"/>
    <text class="module-code" y="-41">INST</text>
    <text class="module-name" y="-22">Instandhaltung</text>
    <g transform="translate(0 38)">
      <use href="#badge"/>
      <path class="icon" stroke-width="4" d="M-13,13 L8,-8 M13,13 L-6,-6"/>
      <path class="icon" d="M8,-8 A6,6 0 1 1 14,-14 M-6,-6 L-13,-13 L-10,-16 L-3,-9"/>
    </g>
  </g>

  <g class="module m-alarm" transform="translate(707 319)">
    <use class="tile" href="#tile-shape" filter="url(#tile-shadow)"/>
    <use class="band-top" href="#band-top"/><use class="band-bottom" href="#band-bottom"/>
    <text class="module-code" y="-41">ALARM</text>
    <text class="module-name" y="-22">Alarmierung</text>
    <g transform="translate(0 38)">
      <use href="#badge"/>
      <circle class="icon-fill" r="5"/>
      <path class="icon" d="M-9,-8 A12,12 0 0 0 -9,8 M9,-8 A12,12 0 0 1 9,8 M-15,-13 A20,20 0 0 0 -15,13 M15,-13 A20,20 0 0 1 15,13"/>
    </g>
  </g>

  <g class="module m-dok" transform="translate(920 319)">
    <use class="tile" href="#tile-shape" filter="url(#tile-shadow)"/>
    <use class="band-top" href="#band-top"/><use class="band-bottom" href="#band-bottom"/>
    <text class="module-code" y="-41">DOK</text>
    <text class="module-name" y="-21">Dokumentenmanagement</text>
    <g transform="translate(0 38)">
      <use href="#badge"/>
      <path class="icon" d="M-11,-16 H5 L12,-9 V16 H-11 Z M-6,-5 H7 M-6,1 H7 M-6,7 H7"/>
    </g>
  </g>

  <!-- Row 3 -->
  <g class="module m-mde" transform="translate(177 501)">
    <use class="tile" href="#tile-shape" filter="url(#tile-shadow)"/>
    <use class="band-top" href="#band-top"/><use class="band-bottom" href="#band-bottom"/>
    <text class="module-code" y="-41">MDE</text>
    <text class="module-name" y="-21">Maschinendatenerfassung</text>
    <g transform="translate(0 38)">
      <use href="#badge"/>
      <circle class="icon" cx="-8" cy="5" r="7" stroke-dasharray="3 2"/>
      <circle class="icon" cx="-8" cy="5" r="2.5"/>
      <circle class="icon" cx="2" cy="-9" r="5" stroke-dasharray="3 2"/>
      <path class="icon" d="M4,13 L16,-3 L19,0 L7,16 L3,17 Z"/>
    </g>
  </g>

  <g class="module m-tnt" transform="translate(389 501)">
    <use class="tile" href="#tile-shape" filter="url(#tile-shadow)"/>
    <use class="band-top" href="#band-top"/><use class="band-bottom" href="#band-bottom"/>
    <text class="module-code" y="-41">TNT</text>
    <text class="module-name" y="-21">Traceability</text>
    <g transform="translate(0 38)">
      <use href="#badge"/>
      <path class="icon" stroke-width="3.4" d="M-16,-8 H-7 C0,-8 2,8 9,8 H14 M-16,8 H-7 C0,8 2,-8 9,-8 H14"/>
      <path class="icon-fill" d="M12,-14 L19,-8 L12,-2 Z M12,2 L19,8 L12,14 Z"/>
    </g>
  </g>

  <g class="module m-pep" transform="translate(601 501)">
    <use class="tile" href="#tile-shape" filter="url(#tile-shadow)"/>
    <use class="band-top" href="#band-top"/><use class="band-bottom" href="#band-bottom"/>
    <text class="module-code" y="-41">PEP</text>
    <text class="module-name" y="-21">Personaleinsatzplanung</text>
    <g transform="translate(0 38)">
      <use href="#badge"/>
      <circle class="icon-fill" cx="-10" cy="-10" r="3.5"/>
      <circle class="icon-fill" cx="10" cy="-10" r="3.5"/>
      <circle class="icon-fill" cx="0" cy="-7" r="4"/>
      <rect class="icon-fill" x="-14" y="-5" width="8" height="14" rx="2"/>
      <rect class="icon-fill" x="6" y="-5" width="8" height="14" rx="2"/>
      <rect class="icon-fill" x="-5" y="-2" width="10" height="19" rx="2"/>
    </g>
  </g>

  <g class="module m-vis" transform="translate(813 501)">
    <use class="tile" href="#tile-shape" filter="url(#tile-shadow)"/>
    <use class="band-top" href="#band-top"/><use class="band-bottom" href="#band-bottom"/>
    <text class="module-code" y="-41">VIS</text>
    <text class="module-name" y="-21">Visualisierung</text>
    <g transform="translate(0 38)">
      <use href="#badge"/>
      <path class="icon" stroke-width="3" d="M-19,0 C-10,-12 10,-12 19,0 C10,12 -10,12 -19,0 Z"/>
      <circle class="icon" r="5.5" stroke-width="3"/>
    </g>
  </g>

  <g class="module m-em" transform="translate(1027 501)">
    <use class="tile" href="#tile-shape" filter="url(#tile-shadow)"/>
    <use class="band-top" href="#band-top"/><use class="band-bottom" href="#band-bottom"/>
    <text class="module-code" y="-41">EM</text>
    <text class="module-name" y="-21">Energiemonitoring</text>
    <g transform="translate(0 38)">
      <use href="#badge"/>
      <rect class="icon" x="-17" y="-8" width="31" height="16" rx="2"/>
      <rect class="icon-fill" x="16" y="-4" width="3" height="8"/>
      <path class="icon-fill" d="M-14,-5 H8 L3,5 H-14 Z"/>
    </g>
  </g>

  <!-- Row 4 -->
  <g class="module m-plan" transform="translate(284 682)">
    <use class="tile" href="#tile-shape" filter="url(#tile-shadow)"/>
    <use class="band-top" href="#band-top"/><use class="band-bottom" href="#band-bottom"/>
    <text class="module-code" y="-41">PLAN</text>
    <text class="module-name" y="-21">Feinplanung/Leitstand</text>
    <g transform="translate(0 38)">
      <use href="#badge"/>
      <rect class="icon" x="-15" y="-11" width="30" height="25" rx="3"/>
      <path class="icon" d="M-15,-4 H15 M-8,-15 V-9 M8,-15 V-9"/>
      <g class="icon-fill">
        <rect x="-11" y="0" width="5" height="4"/><rect x="-3" y="0" width="5" height="4"/><rect x="5" y="0" width="5" height="4"/>
        <rect x="-11" y="6" width="5" height="4"/><rect x="-3" y="6" width="5" height="4"/><rect x="5" y="6" width="5" height="4"/>
      </g>
    </g>
  </g>

  <g class="module m-mpze" transform="translate(496 682)">
    <use class="tile" href="#tile-shape" filter="url(#tile-shadow)"/>
    <use class="band-top" href="#band-top"/><use class="band-bottom" href="#band-bottom"/>
    <text class="module-code" y="-41">MPZE</text>
    <text class="module-name" y="-21">Personalzeiterfassung</text>
    <g transform="translate(0 38)">
      <use href="#badge"/>
      <circle class="icon" r="17" stroke-width="3"/>
      <path class="icon" d="M-9,-3 L0,2 L10,-5"/>
    </g>
  </g>

  <g class="module m-dnc" transform="translate(708 682)">
    <use class="tile" href="#tile-shape" filter="url(#tile-shadow)"/>
    <use class="band-top" href="#band-top"/><use class="band-bottom" href="#band-bottom"/>
    <text class="module-code" y="-41">DNC</text>
    <text class="module-name" y="-21">Rezepturen/DNC</text>
    <g transform="translate(0 38)">
      <use href="#badge"/>
      <path class="icon" stroke-width="2" d="M0,-10 V0 M-12,6 V0 H12 V6 M0,0 V6"/>
      <g class="icon-fill">
        <rect x="-5" y="-18" width="10" height="9"/>
        <rect x="-17" y="6" width="10" height="9"/><rect x="-5" y="6" width="10" height="9"/><rect x="7" y="6" width="10" height="9"/>
      </g>
    </g>
  </g>

  <g class="module m-log" transform="translate(921 682)">
    <use class="tile" href="#tile-shape" filter="url(#tile-shadow)"/>
    <use class="band-top" href="#band-top"/><use class="band-bottom" href="#band-bottom"/>
    <text class="module-code" y="-41">LOG</text>
    <text class="module-name" y="-21">Logistik</text>
    <g transform="translate(0 38)">
      <use href="#badge"/>
      <path class="icon-fill" d="M-18,-10 H7 V-5 H12 L18,2 V9 H-18 Z"/>
      <circle cx="-9" cy="10" r="4" fill="#fff" stroke="var(--dark)" stroke-width="2.4"/>
      <circle cx="10" cy="10" r="4" fill="#fff" stroke="var(--dark)" stroke-width="2.4"/>
    </g>
  </g>
</svg>
</body>
</html>
```